Harlow Pennick Group Business Cards

We have a new logo, and want to design new business cards with it. We are 21 years in business, and want a fresh but professional look, so not a lot of extra stuff on the card. We are a recruiting and staffing firm focused on placing accounting and finance professionals in the Dallas TX area. I've attached our new logo that should be displayed on the cards. Here is what I think we want on the cards:
Ned Varcombe, CPA
Partner and Managing Director
8262 Quarry Mill Rd.
Suite 610
Dallas, TX 75391
O 214-583-9071
M 214-690-1482
ned@harlowpennick-example.com
www.harlowpennick-example.com

```html
<!DOCTYPE html>
<html lang="en">
<head>
<meta charset="utf-8">
<title>Harlow Pennick Group – Business Cards</title>
<link rel="stylesheet" href="https://fonts.googleapis.com/css2?family=Montserrat:wght@500;600;700&display=swap">
<style>
  :root {
    --brand-blue: #2442a0;
    --brand-blue-light: #4d6cc4;
    --card-white: #ffffff;
    --backdrop: #3a3a3a;
    --ink: #2442a0;
  }
  * { box-sizing: border-box; margin: 0; padding: 0; }
  html, body {
    width: 1200px; height: 1074px; overflow: hidden;
    background: var(--backdrop);
    font-family: "Montserrat", sans-serif;
  }
  .sheet {
    width: 1200px; height: 1074px;
    display: flex; flex-direction: column; align-items: center; justify-content: center;
    gap: 44px;
  }
  .card {
    position: relative;
    width: 820px; height: 469px;
    overflow: hidden;
  }
  .card-front {
    background: var(--brand-blue);
    display: flex; align-items: center; justify-content: center;
  }
  .brand-name {
    display: flex; align-items: center; gap: 16px;
    font-weight: 700; text-transform: uppercase; letter-spacing: 0.04em;
  }
  .brand-mark { width: 22px; height: 22px; background: currentColor; flex: none; }
  .card-front .brand-name { color: var(--card-white); font-size: 40px; }
  .card-back { background: var(--card-white); color: var(--ink); }
  .card-back .brand-name {
    position: absolute; top: 64px; right: 48px;
    font-size: 22px;
  }
  .divider {
    position: absolute; left: 56px; top: 252px;
    width: 716px; height: 2px; background: var(--brand-blue);
  }
  .holder { position: absolute; left: 56px; top: 190px; }
  .holder-name { font-size: 32px; font-weight: 600; line-height: 1.1; }
  .holder-title { font-size: 16px; font-weight: 600; margin-top: 4px; }
  .contact-list {
    position: absolute; left: 56px; top: 272px;
    list-style: none; font-size: 19px; font-weight: 500; line-height: 1.75;
  }
  .contact-list li { display: flex; align-items: center; gap: 12px; }
  .contact-list svg { width: 18px; height: 18px; fill: var(--brand-blue); flex: none; }
  .address {
    position: absolute; right: 48px; top: 272px;
    font-size: 18px; font-weight: 500; line-height: 1.6; font-style: normal;
  }
  .footer-band { position: absolute; left: 0; bottom: 0; width: 820px; height: 80px; }
  .website {
    position: absolute; right: 36px; bottom: 32px;
    color: var(--card-white); font-size: 17px; font-weight: 500;
    white-space: nowrap;
  }
</style>
</head>
<body>
<main class="sheet">
  <section class="card card-front" aria-label="Card front">
    <div class="brand-name"><span class="brand-mark"></span>Harlow Pennick Group</div>
  </section>

  <section class="card card-back" aria-label="Card back">
    <div class="brand-name"><span class="brand-mark"></span>Harlow Pennick Group</div>

    <div class="holder">
      <h1 class="holder-name">Ned Varcombe, CPA</h1>
      <p class="holder-title">Partner and Managing Director</p>
    </div>
    <div class="divider"></div>

    <ul class="contact-list">
      <li><svg viewBox="0 0 24 24" aria-hidden="true"><path d="M6.6 10.8a15.1 15.1 0 0 0 6.6 6.6l2.2-2.2c.3-.3.7-.4 1-.2 1.1.4 2.3.6 3.6.6.6 0 1 .4 1 1V20c0 .6-.4 1-1 1A17 17 0 0 1 3 4c0-.6.4-1 1-1h3.5c.6 0 1 .4 1 1 0 1.3.2 2.5.6 3.6.1.3 0 .7-.2 1z"/></svg>214-583-9071</li>
      <li><svg viewBox="0 0 24 24" aria-hidden="true"><path d="M8 1h8a2 2 0 0 1 2 2v18a2 2 0 0 1-2 2H8a2 2 0 0 1-2-2V3a2 2 0 0 1 2-2zm0 3v14h8V4zm4 15.5a1 1 0 1 0 0 2 1 1 0 0 0 0-2z"/></svg>214-690-1482</li>
      <li><svg viewBox="0 0 24 24" aria-hidden="true"><path d="M2 5h20v14H2zm2 2v.5l8 5 8-5V7zm0 2.8V17h16V9.8l-8 5z"/></svg>ned@harlowpennick-example.com</li>
    </ul>

    <address class="address">
      8262 Quarry Mill Rd. Suite 610<br>
      Dallas, TX 75391
    </address>

    <svg class="footer-band" viewBox="0 0 820 80" aria-hidden="true">
      <polygon points="0,34 410,34 410,38 0,38" fill="var(--brand-blue-light)"/>
      <polygon points="450,0 820,0 820,80 0,80 0,62 420,62" fill="var(--brand-blue)"/>
    </svg>
    <p class="website">www.harlowpennick-example.com</p>
  </section>
</main>
</body>
</html>
```